Small Local Computer Shop Website Needed

Im after a new website that goes with my brand logo.
We are a small all family run local computer repair company and would like to drive more business via the site.
I have added my old site and one that was in progress also a Facebook link to give you an idea.

I would like to be able to make it stand out more and be easy to navigate.
I am basically a small computer repair shop, we offer in store repairs and upgrades. We also do call outs to your home or business and we also sell laptops,pcs and peripherals.

We do sell Laptops and pcs and although i don't really want to sell directly from the web it would be nice to be able to show what we have on offer on our site, Roughly 20-30 items generally.

Current site
http://byte-vale.com

New Site
http://byte-vale.com/site/

Facebook
http://www.sociabook.com/pages/Byte-Vale/847315902264710

images and files are available.

Many Thanks
Hugo
Byte Vale

Target Market(s)

I cater for all ages!

Industry/Entity Type

It Company

Number of Pages Required

5+ page

Font styles to use
Sans Serif

Requirements
Must have
• Be nice to keep in theme with my Logo.
• Landing page.
• Contact page
• about us
• Laptops (Displaying products currently for sale in store) Generally 10-20 at a time
• Pcs (Displaying products currently for sale in store)
Nice to have
• i would like and easy way for the customers to navigate to my remote support site. ie.
• https://www.remotorhelp.com/
• Easy link to download there trial off shieldwarren antivirus.
• ie http://downloads.shieldwarren.com/partners/rskit/ShieldWarrenDownloader_bytevalekit.exe
• Link to our Repair tracker... When we check in a computer or laptop repair the Customers can see how there jobs progressing by clicking the link. ie http://byte-vale.com/shop/repairstatus/
• would be great if there was a fairly straight forward way to add/ remove pc's and laptops for sale on our site.
• Maybe check our facebook for ideas images etc..
• https://www.sociabook.com/Byte-vale-847315902264710/
Should not have
• The site i currently have i really dislike, so please dont copy that theme.
• Had a few designs with a white banner at the top with my logo.
• Sorry but have decided these are not what i want.
• a darker theme is def more in line with what im looking for.
• Thanks

```html
<!DOCTYPE html>
<html lang="en">
<head>
<meta charset="utf-8">
<title>Byte Vale – Computer Repair</title>
<link href="https://fonts.googleapis.com/css2?family=Roboto:wght@300;400;500;700&display=swap" rel="stylesheet">
<style>
:root{
  --teal-dark:#17536b;
  --teal:#1f6f8e;
  --teal-light:#3a98b8;
  --header-top:#1a1f24;
  --ink:#333a40;
  --muted:#6b737a;
  --line:#c9d3da;
  --services-bg:#eef2f5;
  --footer-bg:#1c1c1c;
  --white:#ffffff;
}
*{box-sizing:border-box;margin:0;padding:0}
html,body{width:1200px;height:2195px;overflow:hidden}
body{font-family:'Roboto',Arial,sans-serif;color:var(--ink);background:var(--white);position:relative}
.abs{position:absolute}

/* header */
.site-header{position:absolute;left:0;top:0;width:1200px;height:110px;
  background:linear-gradient(90deg,var(--header-top) 0%,#1d3a4a 45%,var(--teal) 100%)}
.brand{left:85px;top:28px;font-size:44px;font-weight:700;color:var(--white);letter-spacing:1px;display:flex;align-items:center;gap:14px}
.brand-dot{width:16px;height:16px;border-radius:50%;background:var(--teal-light)}
.topline{left:588px;top:25px;font-size:15px;color:var(--white)}
.social-top{left:962px;top:20px;display:flex;gap:12px}
.social-top span{width:24px;height:24px;border:1.5px solid rgba(255,255,255,.8);border-radius:50%}
.main-nav{left:436px;top:74px;display:flex;align-items:center;font-size:16px;color:var(--white)}
.main-nav a{color:var(--white);text-decoration:none;padding:0 24px;border-right:1px solid rgba(255,255,255,.6);line-height:16px}
.main-nav a:last-child{border-right:none}
.main-nav a.active{font-weight:700;text-decoration:underline;text-underline-offset:6px}
.search-btn{left:1078px;top:66px;width:34px;height:34px;border-radius:50%;background:var(--white);display:flex;align-items:center;justify-content:center}

/* hero */
.hero{left:0;top:110px;width:1200px;height:524px;
  background:linear-gradient(120deg,#b9c6cf 0%,#d9e2e8 35%,#9fb0bd 70%,#5e6f7c 100%)}
.estimate{left:285px;top:220px;width:625px;height:306px;background:var(--white);border-top:5px solid var(--teal-dark);box-shadow:0 4px 18px rgba(0,0,0,.25)}
.estimate h2{position:absolute;top:30px;width:100%;text-align:center;font-size:22px;font-weight:500;color:var(--teal)}
.field{position:absolute;border:1.5px solid var(--teal-light);font-size:12px;color:var(--teal);padding:0 12px;display:flex;align-items:center}
.btn-estimate{position:absolute;left:52px;top:211px;width:254px;height:46px;background:var(--teal-dark);color:var(--white);font-size:15px;font-weight:500;display:flex;align-items:center;justify-content:center;letter-spacing:.5px}

/* repair intro */
.devices{left:122px;top:730px;width:420px;height:250px;border-radius:4px;
  background:linear-gradient(160deg,#e9edf0 0%,#bfc7cd 55%,#8f999f 100%)}
.intro-title{left:588px;top:758px;font-size:28px;font-weight:400;color:#222}
.intro-text{left:588px;top:803px;width:500px;font-size:12.5px;line-height:18.5px;color:var(--muted)}
.intro-phone{left:588px;top:932px;display:flex;align-items:center;gap:14px;font-size:32px;font-weight:500;color:var(--teal-dark)}

/* services */
.services{left:0;top:1050px;width:1200px;height:540px;background:var(--services-bg)}
.service{position:absolute;width:380px}
.service h3{font-size:16px;font-weight:500;color:var(--teal-dark);margin-bottom:10px}
.service p{font-size:11.5px;line-height:17px;color:var(--muted);margin-bottom:4px}
.service .more{font-size:11.5px;color:var(--teal-dark)}
.service-icon{position:absolute;width:84px;height:84px;border-radius:50%;background:var(--white);border:1.5px solid var(--line);display:flex;align-items:center;justify-content:center}
.service-icon.featured{background:var(--teal-dark);border-color:var(--teal-dark)}
.icon-link{position:absolute;width:1.5px;background:var(--line)}
.icon-arm{position:absolute;height:1.5px;background:var(--line)}

/* about */
.about-text{left:83px;top:1650px;width:530px;font-size:17px;line-height:30px;color:var(--muted)}
.about-text p{margin-bottom:30px}
.technician{left:654px;top:1655px;width:470px;height:360px;
  background:linear-gradient(135deg,#f2f2f2 0%,#9aa3a8 40%,#3b3f42 75%,#e8e8e8 100%)}

/* footer */
.site-footer{left:0;top:2068px;width:1200px;height:127px;background:var(--footer-bg);color:var(--white)}
.foot-col{position:absolute;top:22px}
.foot-col h4{font-size:15px;font-weight:500;letter-spacing:.5px;margin-bottom:12px}
.foot-col p{font-size:11px;line-height:17px;color:#d8d8d8}
.foot-social{display:flex;gap:10px}
.foot-social span{width:24px;height:24px;border-radius:50%;background:var(--white)}
.foot-brand{left:905px;top:22px;font-size:34px;font-weight:700;color:var(--white)}
.copyright{left:905px;top:80px;font-size:11px;color:#d8d8d8}
</style>
</head>
<body>

<header class="site-header">
  <div class="abs brand"><span class="brand-dot"></span>Byte Vale</div>
  <div class="abs topline">Call Us Today! 01392 555 014 | sales@byte-vale.com</div>
  <div class="abs social-top"><span></span><span></span><span></span><span></span><span></span></div>
  <nav class="abs main-nav">
    <a class="active" href="#">Home</a><a href="#">About us</a><a href="#">Laptops</a><a href="#">Pcs</a><a href="#">Store</a><a href="#">Contact us</a>
  </nav>
  <div class="abs search-btn">
    <svg width="16" height="16" viewBox="0 0 16 16"><circle cx="6.5" cy="6.5" r="4.5" fill="none" stroke="#17536b" stroke-width="2"/><line x1="10" y1="10" x2="14" y2="14" stroke="#17536b" stroke-width="2"/></svg>
  </div>
</header>

<section class="abs hero" role="img" aria-label="Photo of a frustrated office worker lifting a computer monitor at her desk"></section>

<form class="abs estimate">
  <h2>Before you do this. Let us help solve your problem.</h2>
  <div class="field" style="left:52px;top:95px;width:254px;height:46px">Name</div>
  <div class="field" style="left:322px;top:95px;width:254px;height:46px">Phone</div>
  <div class="field" style="left:52px;top:153px;width:254px;height:46px">Email</div>
  <div class="field" style="left:322px;top:153px;width:254px;height:104px;align-items:flex-start;padding-top:14px">Describe your problem</div>
  <div class="btn-estimate">GET AN ESTIMATE</div>
</form>

<div class="abs devices" role="img" aria-label="Illustration of a desktop monitor and a laptop on a circuit board background"></div>
<h2 class="abs intro-title">We offer professional repair service</h2>
<p class="abs intro-text">Our technicians diagnose and fix desktops, laptops and tablets quickly and at fair prices. We handle screen swaps, virus removal, data transfers, upgrades and full rebuilds in store or at your door. Every job gets a clear quote before work starts, regular updates while we repair, and a friendly warranty once it is done.</p>
<div class="abs intro-phone">
  <svg width="30" height="30" viewBox="0 0 24 24"><path fill="#9aa3a8" d="M6.6 10.8c1.4 2.8 3.8 5.1 6.6 6.6l2.2-2.2c.3-.3.7-.4 1-.2 1.1.4 2.3.6 3.6.6.6 0 1 .4 1 1V20c0 .6-.4 1-1 1C10.6 21 3 13.4 3 4c0-.6.4-1 1-1h3.5c.6 0 1 .4 1 1 0 1.3.2 2.5.6 3.6.1.3 0 .7-.2 1z"/></svg>
  908-555-0182
</div>

<section class="abs services">
  <div class="icon-link" style="left:520px;top:122px;height:300px"></div>
  <div class="icon-link" style="left:1073px;top:122px;height:300px"></div>
  <div class="icon-arm" style="left:520px;top:270px;width:0"></div>

  <div class="service" style="left:83px;top:80px">
    <h3>Local &amp; Nationwide Repair</h3>
    <p>Get the fast, reliable and affordable computer repair services that you need at our New Jersey repair center or choose from the wide selection of computer maintenance services that we can deliver.</p>
    <span class="more">Read More</span>
  </div>
  <div class="service-icon featured" style="left:478px;top:80px">
    <svg width="38" height="38" viewBox="0 0 24 24" fill="none" stroke="#fff" stroke-width="1.6"><path d="M14.5 6.5a4 4 0 0 0 5 5L12 19l-3-3 7.5-7.5z"/><path d="M4 20l5-5"/><circle cx="6" cy="6" r="2.5"/></svg>
  </div>

  <div class="service" style="left:639px;top:80px">
    <h3>Managed Services</h3>
    <p>We provide 24/7 remote support for your critical business systems without sacrificing quality. Get the remote computer support &amp; monitoring services that your enterprise needs to keep its computer.</p>
    <span class="more">Read More</span>
  </div>
  <div class="service-icon" style="left:1031px;top:80px">
    <svg width="34" height="34" viewBox="0 0 24 24" fill="none" stroke="#555" stroke-width="1.5"><path d="M16 3l5 5-11 11H5v-5z"/><path d="M13 6l5 5"/></svg>
  </div>

  <div class="service" style="left:83px;top:226px">
    <h3>Remote Support</h3>
    <p>Did you know that many of your computer repair and maintenance services needs can be done without you leaving the comfort of your home of office? We can solve many different kinds.</p>
    <span class="more">Read More</span>
  </div>
  <div class="service-icon" style="left:478px;top:226px">
    <svg width="34" height="34" viewBox="0 0 24 24" fill="none" stroke="#555" stroke-width="1.5"><path d="M5 13v-2a7 7 0 0 1 14 0v2"/><rect x="3" y="12" width="4" height="6" rx="1"/><rect x="17" y="12" width="4" height="6" rx="1"/><path d="M19 18c0 2-2 3-5 3"/></svg>
  </div>

  <div class="service" style="left:639px;top:226px">
    <h3>Website Design &amp; Maintenance</h3>
    <p>We offer complete business website solutions with optional on-going maintenance &amp; support. Establish your online business presence the right way, the first time around with the customized.</p>
    <span class="more">Read More</span>
  </div>
  <div class="service-icon" style="left:1031px;top:226px">
    <svg width="36" height="36" viewBox="0 0 24 24" fill="none" stroke="#555" stroke-width="1.5"><rect x="3" y="5" width="18" height="11" rx="1"/><path d="M9 20h6M12 16v4"/></svg>
  </div>

  <div class="service" style="left:83px;top:382px">
    <h3>Data Recovery</h3>
    <p>Get your most important files back with the in-store data recovery and storage device replacement services that we offer at our New Jersey repair center. Rest easy.</p>
    <span class="more">Read More</span>
  </div>
  <div class="service-icon" style="left:478px;top:382px">
    <svg width="32" height="32" viewBox="0 0 24 24" fill="none" stroke="#555" stroke-width="1.5"><path d="M4 4h13l3 3v13H4z"/><rect x="8" y="4" width="7" height="5"/><rect x="7" y="13" width="10" height="7"/></svg>
  </div>

  <div class="service" style="left:639px;top:382px">
    <h3>Remote Help Desk for Businesses</h3>
    <p>Avoid the hassle of hiring and managing an in-house IT support staff with our reliable U.S. Based remote computer help desk service plans. Our remote help desk services.</p>
    <span class="more">Read More</span>
  </div>
  <div class="service-icon" style="left:1031px;top:382px">
    <svg width="34" height="34" viewBox="0 0 24 24" fill="none" stroke="#555" stroke-width="1.5"><circle cx="12" cy="9" r="4"/><path d="M5 21c1-4 4-6 7-6s6 2 7 6"/><path d="M7 9a5 5 0 0 1 10 0"/></svg>
  </div>
</section>

<div class="abs about-text">
  <p>Vale Computers deliver expert onsite computer services to small businesses and home owners in Southern Tasmania. We specialise in IT security, custom built computers and general computer repair.</p>
  <p>Our expert staff will also help you with training and pre-purchase advise to what suits your business or family best, and what will also future proof you in the areas where your system will be utilised the most. The best thing is that WE'LL COME TO YOU.</p>
  <p>We prefer to do most of our support onsite, but sometimes it is necessary to take your computer(s) away to be repaired at our office.</p>
</div>
<div class="abs technician" role="img" aria-label="Photo of a technician repairing the inside of a desktop computer tower"></div>

<footer class="abs site-footer">
  <div class="foot-col" style="left:83px">
    <h4>LOCATION</h4>
    <p>22 Ashgrove Lane, Exeter,<br>Devon, EX1 0ZZ<br>01392 555 014 Email:sales@byte-vale.com</p>
  </div>
  <div class="foot-col" style="left:395px">
    <h4>CONTACT US</h4>
    <p>Phone: 305-555-0147<br>Email: hello@byte-vale.com</p>
  </div>
  <div class="foot-col" style="left:654px">
    <h4>FOLLOW US</h4>
    <div class="foot-social"><span></span><span></span><span></span><span></span></div>
  </div>
  <div class="abs foot-brand">Byte Vale</div>
  <div class="abs copyright">Copyright 2016 © BYTE VALE</div>
</footer>

</body>
</html>
```